IV Nutritional Clinic Web Design

We are working with Velmo. They are an IV Nutritional Clinic and in need of a new website design.
Some sites to use for inspiration:
https://brightpathcare.example
https://www.mylumarowellness.example
https://www.quenchlounge.example
https://vitrapulse.example
https://www.sola-vita.example/pages/iv-therapy-west-hollywood
https://www.gtoncologycare.example/cancer-care/iv-drips/
https://dripfuelwell.example
https://thrivoramedclinic.example
Thank you for taking the time to consider designing a website for us. We are web developers based in Stockton, CA, USA. Most of our projects go through the same process. Understanding this process may help you win a project with us. We custom-code all of our websites in-house. We don’t have any requirements as to what tools you use for your design, but we prefer Figma files. For any design that we label as four-stars, we send it to the client for review. The client picks the final design they want us to use. Once we complete this process, we will continue to show additional clients all the four-star sites and purchase them later. Your designs will have multiple chances to sell. For better chances of success, we ask that you follow these guidelines.
IMAGES:
If you use any images or icons in the design, we ask that you have a link to the asset so we can purchase the image/icon. Most of the designs we submit do not have the customer’s images on them unless they have some great images. Be creative; show us the feeling you are trying to portray with your image choices. Use any royalty-free site you choose. We subscribe to Korvane and mainly use their images, but we can purchase images outside of Korvane.
PLEASE NOTE: we will not submit designs to clients with watermarks on the images.
FONTS:
We ask that you identify the fonts used in the design. This can be done in a message if you want. We typically use Tessly Type and Korvane Type.
CONTENT:
We're always open to different content and ideas. We often submit designs with stock images so the client can see our vision. We typically take pictures after the website launch to use their images with our vision. Lorem Ipsum is fine for paragraphs, but we ask that you write the headers in correct English. We want to be able to show the vision and identify the sections of the website.
INSPIRATION:
We typically add a couple of links in the brief of websites we like to help you get started in your design.
REVISIONS:
We do not often ask for revisions of the designs unless we see something in the design that may not appeal to the client. If there are slight changes that we want to make, we do that in the development process.
FEEDBACK:
We rarely give feedback on designs during the design process. We are working on many website projects and do not have the time to provide feedback. We usually respond if your request is well thought out and asks specific questions, but a note asking “feedback, please” usually goes unanswered.

```html
<!DOCTYPE html>
<html lang="en">
<head>
<meta charset="utf-8">
<title>Velmo Hydration – IV Nutrition</title>
<link rel="stylesheet" href="https://fonts.googleapis.com/css2?family=Libre+Baskerville:wght@400;700&family=Open+Sans:wght@400;600;700&display=swap">
<style>
:root{
  --navy:#1f4b86;
  --green:#76a845;
  --text:#5d6470;
  --heading:#1f4b86;
  --bg-soft:#f3f4f6;
  --white:#ffffff;
  --orange:#f0862a;
}
*{margin:0;padding:0;box-sizing:border-box}
html,body{width:1200px;height:4841px;overflow:hidden}
body{font-family:"Open Sans",sans-serif;color:var(--text);background:var(--white);position:relative}
.abs{position:absolute}
.serif{font-family:"Libre Baskerville",serif;font-weight:700;color:var(--heading)}
.photo{position:absolute}
.btn-green{position:absolute;background:var(--green);color:#fff;font-size:13px;font-weight:700;display:flex;align-items:center;justify-content:center;border-radius:4px}
.eyebrow{position:absolute;font-size:11px;font-weight:600;color:var(--green);letter-spacing:.3px;display:flex;align-items:center;gap:14px}
.eyebrow::after{content:"";width:50px;height:2px;background:var(--green)}
p.body{font-size:12.5px;line-height:24px}

/* header */
.site-header{position:absolute;left:0;top:0;width:1200px;height:86px;background:#fff;z-index:5}
.top-welcome{left:393px;top:10px;font-size:13px;color:#333}
.top-mail{left:625px;top:6px;font-size:13px;color:#333;display:flex;align-items:center;gap:8px}
.top-mail .ic{width:26px;height:26px;border-radius:50%;border:2px solid var(--navy);display:flex;align-items:center;justify-content:center}
.header-rule{left:0;top:34px;width:1200px;height:1px;background:#e4e4e4}
.logo-badge{left:136px;top:0;width:150px;height:100px;border-radius:50%;background:#fff;box-shadow:0 4px 12px rgba(0,0,0,.12);display:flex;align-items:center;justify-content:center;font-weight:700;font-size:30px;color:var(--navy);z-index:6}
.nav{left:336px;top:54px;display:flex;font-size:12.5px;color:#333}
.nav a{text-decoration:none;color:#333;margin-right:48px}
.nav a.active{color:var(--navy);font-weight:700}
.call-box{left:858px;top:0;width:200px;height:86px;background:var(--navy);color:#fff;display:flex;align-items:center;gap:14px;padding-left:4px}
.call-box .ring{width:38px;height:38px;border-radius:50%;background:#fff;display:flex;align-items:center;justify-content:center;margin-left:-20px}
.call-box small{display:block;font-size:13px}
.call-box strong{font-size:19px}

/* hero */
.hero-photo{left:0;top:86px;width:1200px;height:790px;background:linear-gradient(120deg,#dfe9f1 0%,#b9cad8 40%,#6c8aa6 70%,#c9d3dc 100%)}
.hero-card{left:75px;top:272px;width:476px;height:362px;background:#fff;padding:48px 0 0 48px}
.hero-card .bar{position:absolute;left:0;top:56px;width:6px;height:110px;background:var(--green)}
.hero-card h1{font-size:56px;line-height:68px}
.hero-card p{margin-top:22px;width:400px;font-size:11.5px;line-height:22px}
.hero-edge{left:0;top:760px;width:1200px;height:120px}

/* about */
.collage{left:103px;top:970px;width:470px;height:478px}
.about-text{left:623px}
.features{left:88px;top:1530px;width:1016px;height:216px;background:#fff;border-radius:0 0 80px 80px;box-shadow:0 6px 24px rgba(0,0,0,.10)}
.feature{position:absolute;top:36px;width:300px}
.feature .ic{position:absolute;left:0;top:0;width:64px;height:64px;border-radius:50%;border:3px solid var(--navy);display:flex;align-items:center;justify-content:center}
.feature h3{position:absolute;left:81px;top:8px;font-size:20px}
.feature .sub{position:absolute;left:84px;top:40px;font-size:15px;color:var(--green)}
.feature p{position:absolute;left:81px;top:70px;width:200px;font-size:12px;line-height:23px}

/* services */
.services-bg{left:0;top:1790px;width:1200px;height:736px;background:var(--bg-soft)}
.arrow-btn{position:absolute;top:1870px;width:43px;height:62px;background:#fff;box-shadow:0 2px 8px rgba(0,0,0,.12);display:flex;align-items:center;justify-content:center;border-radius:4px}
.service{position:absolute;top:1972px;width:323px;height:376px}
.service .img{position:absolute;left:0;top:0;width:323px;height:234px}
.service .box{position:absolute;left:20px;top:178px;width:283px;height:198px;background:#fff;box-shadow:0 4px 14px rgba(0,0,0,.10);padding:24px 20px 0 40px}
.service .box h3{font-size:17px;margin-bottom:16px;white-space:nowrap}
.service .box p{font-size:12px;line-height:24px;width:215px}
.service .box .more{display:block;margin-top:16px;font-size:14px;font-weight:700;color:var(--green)}
.service.featured .box{background:var(--green)}
.service.featured .box h3,.service.featured .box p,.service.featured .box .more{color:#fff}
.btn-outline{left:512px;top:2390px;width:168px;height:48px;border:2px solid var(--navy);border-radius:6px;display:flex;align-items:center;justify-content:center;font-size:13px;font-weight:600;color:var(--navy)}

/* revive */
.point{position:absolute;width:260px}
.point .ic{position:absolute;left:0;top:0;width:36px;height:36px}
.point h4{position:absolute;left:64px;top:0;font-size:14px;color:var(--navy);font-weight:700}
.point p{position:absolute;left:64px;top:28px;width:190px;font-size:12px;line-height:24px}

/* testimonials */
.testi-bg{left:0;top:3160px;width:1200px;height:740px;background:var(--bg-soft)}
.testi{position:absolute;top:3390px;width:323px}
.testi .card{position:absolute;left:0;top:0;width:323px;height:263px;background:#fff;box-shadow:0 4px 12px rgba(0,0,0,.08);text-align:center;padding-top:60px}
.testi .avatar{position:absolute;left:128px;top:-34px;width:66px;height:66px;border-radius:50%;background:linear-gradient(#dfe6ee,#9fb3c8);border:3px solid #fff}
.testi .stars{color:var(--orange);font-size:18px;letter-spacing:10px}
.testi .card p{margin:18px auto 0;width:230px;font-size:12.5px;line-height:24px}
.testi .quote{position:absolute;left:126px;top:225px;width:70px;height:38px;border-radius:35px 35px 0 0;background:var(--navy);display:flex;align-items:center;justify-content:center;color:#fff;font-family:"Libre Baskerville",serif;font-size:30px;font-weight:700;padding-top:12px}
.testi .name{position:absolute;left:0;top:290px;width:323px;text-align:center;font-size:16px;font-weight:700;color:#333}
.testi .city{position:absolute;left:0;top:318px;width:323px;text-align:center;font-size:12.5px}

/* connect */
.connect-photo{left:0;top:3897px;width:1200px;height:501px;background:linear-gradient(90deg,#e7e2da 0%,#d8d1c6 35%,#c9c4bc 60%,#b8c1c6 100%)}
.connect-figure{left:170px;top:3765px;width:440px;height:633px;background:linear-gradient(#e9e6e2,#cfc3b4);border-radius:200px 200px 0 0;opacity:.7}
.connect-card{left:652px;top:3976px;width:460px;height:479px;background:var(--navy);border:4px solid #fff;outline:2px solid var(--navy);border-radius:14px;padding:40px 32px 0;color:#fff;text-align:center}
.connect-card h2{font-size:27px;font-weight:700}
.connect-card p{font-size:12.5px;line-height:18px;margin-top:10px}
.field{height:44px;margin-top:30px;background:#3f68a0;border-radius:4px;text-align:left;padding:15px 0 0 26px;font-size:10px;letter-spacing:.3px}
.book{margin-top:40px;height:46px;background:#fff;border-radius:4px;color:var(--navy);font-size:15px;display:flex;align-items:center;justify-content:center}

/* footer */
.footer-bg{left:0;top:4455px;width:1200px;height:386px;background:var(--bg-soft)}
.footer-logo{left:112px;top:4566px;font-size:46px;font-weight:700;color:var(--navy);letter-spacing:1px;line-height:1}
.f-title{position:absolute;top:4554px;font-size:14px;font-weight:600;color:var(--navy);padding-bottom:12px;border-bottom:1px solid #ccd2da}
.f-list{position:absolute;font-size:13.5px;line-height:32px;color:#555}
.f-row{position:absolute;font-size:13.5px;line-height:22px;color:#555;display:flex;gap:14px;align-items:flex-start}
.social{position:absolute;top:4670px;width:26px;height:26px;border-radius:50%;background:#fff;border:1px solid #dde}
.newsletter{left:859px;top:4660px;width:246px;height:36px;border:1px solid #ccd;background:#fff}
.newsletter span{position:absolute;left:16px;top:10px;font-size:11px;color:#888}
.newsletter b{position:absolute;right:0;top:0;width:100px;height:34px;background:var(--green);color:#fff;font-size:12px;display:flex;align-items:center;justify-content:center}
.footer-rule{left:112px;top:4775px;width:976px;height:1px;background:#ccd2da}
.copyright{left:0;top:4800px;width:1200px;text-align:center;font-size:13px;color:var(--navy)}
</style>
</head>
<body>

<header class="site-header">
  <div class="abs top-welcome">WELCOME</div>
  <div class="abs top-mail"><span class="ic"><svg width="12" height="10" viewBox="0 0 12 10"><rect x="0.5" y="0.5" width="11" height="9" fill="none" stroke="#1f4b86"/><path d="M1 1l5 4 5-4" fill="none" stroke="#1f4b86"/></svg></span>hello@velmo.example</div>
  <div class="abs header-rule"></div>
  <nav class="abs nav">
    <a class="active">HOME</a><a>About Us</a><a>Treatments</a><a>Fees</a><a>New Patients</a>
  </nav>
  <div class="abs call-box">
    <span class="ring"><svg width="18" height="18" viewBox="0 0 24 24"><path d="M6.6 10.8a15 15 0 006.6 6.6l2.2-2.2a1 1 0 011-.25 11.4 11.4 0 003.6.6 1 1 0 011 1V20a1 1 0 01-1 1A17 17 0 013 4a1 1 0 011-1h3.5a1 1 0 011 1 11.4 11.4 0 00.6 3.6 1 1 0 01-.25 1z" fill="#76a845"/></svg></span>
    <div><small>Call us today at</small><strong>(425) 555-0147</strong></div>
  </div>
</header>
<div class="abs logo-badge">VELMO</div>

<section>
  <div class="photo hero-photo" role="img" aria-label="Clinician attending to a smiling senior patient reclining in a treatment chair"></div>
  <div class="abs hero-card">
    <span class="bar"></span>
    <h1 class="serif">IV Nutrition,<br>Done Right</h1>
    <p>Lorem ipsum dolor sit amet, consectetur adipiscing elit, sed do eiusmod tempor incididunt ut labore et dolore magna aliqua. Ut enim</p>
    <div class="btn-green" style="left:48px;top:298px;width:168px;height:48px">Contact Us</div>
  </div>
  <svg class="abs hero-edge" viewBox="0 0 1200 120" preserveAspectRatio="none">
    <path d="M0 40 C400 130 800 0 1200 70 L1200 120 L0 120Z" fill="#fff"/>
  </svg>
</section>

<section>
  <svg class="abs collage" viewBox="0 0 470 478" role="img" aria-label="Doctor writing notes, masked clinician with patient, and smiling young child">
    <defs>
      <linearGradient id="g1" x1="0" y1="0" x2="1" y2="1"><stop offset="0" stop-color="#c9d6e2"/><stop offset="1" stop-color="#6f8aa5"/></linearGradient>
      <linearGradient id="g2" x1="0" y1="0" x2="1" y2="1"><stop offset="0" stop-color="#d6e3ec"/><stop offset="1" stop-color="#87a6bd"/></linearGradient>
      <linearGradient id="g3" x1="0" y1="0" x2="1" y2="1"><stop offset="0" stop-color="#5f8fb0"/><stop offset="1" stop-color="#e7c9b4"/></linearGradient>
    </defs>
    <path d="M60 0 H302 V314 H0 V60 A60 60 0 0 1 60 0Z" fill="url(#g1)"/>
    <path d="M327 22 H385 A32 32 0 0 1 417 54 V144 H327Z" fill="url(#g2)"/>
    <path d="M165 162 H470 V400 A78 78 0 0 1 392 478 H165Z" fill="url(#g3)"/>
    <circle cx="186" cy="296" r="48" fill="#1f4b86"/>
    <circle cx="186" cy="296" r="26" fill="none" stroke="#fff" stroke-width="3"/>
    <circle cx="186" cy="296" r="14" fill="none" stroke="#fff" stroke-width="3"/>
    <circle cx="186" cy="296" r="5" fill="#fff"/>
  </svg>
  <div class="eyebrow" style="left:624px;top:990px">ABOUT US</div>
  <h2 class="abs serif about-text" style="top:1028px;font-size:38px;line-height:60px">Vital Nutrients,<br>Amplified Wellness</h2>
  <p class="abs body about-text" style="top:1155px;width:440px">Lorem ipsum dolor sit amet, consectetur adipiscing elit, sed do eiusmod tempor incididunt ut labore et dolore magna aliqua. Ut enim ad min im veniam, quis nostrud exercitation ullamco laboris nisi ut aliquip ex ea commodo consequat. Duis aute irure dolor in reprehenderit in voluptate velit esse cillum dolore eu fugiat nulla pariatur. Excepteur sint occaecat cupidatat non proident, sunt in culpa qui officia deserunt mollit anim id est laborum.</p>
  <div class="btn-green" style="left:624px;top:1346px;width:170px;height:46px">Contact Us</div>

  <div class="abs features">
    <div class="feature" style="left:58px">
      <span class="ic"><svg width="28" height="28" viewBox="0 0 28 28"><circle cx="14" cy="14" r="10" fill="none" stroke="#1f4b86" stroke-width="2" stroke-dasharray="3 3"/></svg></span>
      <h3 class="serif">Innovative</h3><span class="sub">Lorem Ipsum</span>
      <p>Lorem ipsum dolor sit amet, consectetur adipiscing elit, se do eiusmod tempor e</p>
    </div>
    <div class="feature" style="left:366px">
      <span class="ic"><svg width="28" height="28" viewBox="0 0 28 28"><path d="M14 4v8M14 16v8M4 14h8M16 14h8" stroke="#1f4b86" stroke-width="2.5"/></svg></span>
      <h3 class="serif">Experienced</h3><span class="sub">Lorem Ipsum</span>
      <p>Lorem ipsum dolor sit amet, consectetur adipiscing elit, se do eiusmod tempor e</p>
    </div>
    <div class="feature" style="left:676px">
      <span class="ic"><svg width="28" height="28" viewBox="0 0 28 28"><path d="M6 16a8 8 0 0116 0" fill="none" stroke="#1f4b86" stroke-width="2.5"/><rect x="4" y="15" width="5" height="8" rx="2" fill="#1f4b86"/><rect x="19" y="15" width="5" height="8" rx="2" fill="#1f4b86"/></svg></span>
      <h3 class="serif">Available 24/7</h3><span class="sub">Lorem Ipsum</span>
      <p>Lorem ipsum dolor sit amet, consectetur adipiscing elit, se do eiusmod tempor e</p>
    </div>
  </div>
</section>

<section>
  <div class="abs services-bg"></div>
  <div class="eyebrow" style="left:98px;top:1852px">ABOUT US</div>
  <h2 class="abs serif" style="left:96px;top:1890px;font-size:38px">Services We Provide</h2>
  <div class="arrow-btn" style="left:1005px"><svg width="10" height="14" viewBox="0 0 10 14"><path d="M8 1L2 7l6 6" fill="none" stroke="#222" stroke-width="2.5"/></svg></div>
  <div class="arrow-btn" style="left:1058px"><svg width="10" height="14" viewBox="0 0 10 14"><path d="M2 1l6 6-6 6" fill="none" stroke="#222" stroke-width="2.5"/></svg></div>

  <div class="service" style="left:90px">
    <div class="img" role="img" aria-label="Dentist with gloved hand treating a patient" style="background:linear-gradient(135deg,#e5ecf2,#9fb2c4)"></div>
    <div class="box"><h3 class="serif">Performance Boosters</h3><p>Lorem ipsum dolor sit amet, consectetur adipiscing elit, sed do eiusmod tempor incididunt ut nn</p><span class="more">Read More</span></div>
  </div>
  <div class="service featured" style="left:436px">
    <div class="img" role="img" aria-label="Smiling woman seated in a clinic chair" style="background:linear-gradient(135deg,#c6d7e2,#d79a5a)"></div>
    <div class="box"><h3 class="serif">Hydration Therapy</h3><p>Lorem ipsum dolor sit amet, consectetur adipiscing elit, sed do eiusmod tempor incididunt ut nn</p><span class="more">Read More</span></div>
  </div>
  <div class="service" style="left:785px">
    <div class="img" role="img" aria-label="Laughing senior couple at home" style="background:linear-gradient(135deg,#dfe7d8,#b8b4a8)"></div>
    <div class="box"><h3 class="serif">Detox Infusions</h3><p>Lorem ipsum dolor sit amet, consectetur adipiscing elit, sed do eiusmod tempor incididunt ut nn</p><span class="more">Read More</span></div>
  </div>
  <div class="abs btn-outline">Contact Us</div>
</section>

<section>
  <div class="eyebrow" style="left:93px;top:2610px">ABOUT US</div>
  <h2 class="abs serif" style="left:92px;top:2644px;font-size:38px;line-height:60px">Revive, Restore,<br>Replenish</h2>
  <p class="abs body" style="left:93px;top:2775px;width:450px;font-size:12px">Lorem ipsum dolor sit amet, consectetur adipiscing elit, sed do eiusmo d tempor incididunt ut labore et dolore magna aliqua. Ut enim ad min im veniam, quis nostrud exercitation jj</p>

  <div class="point" style="left:104px;top:2880px">
    <svg class="ic" viewBox="0 0 36 36"><rect x="3" y="5" width="8" height="8" fill="none" stroke="#76a845" stroke-width="2.5"/><rect x="3" y="23" width="8" height="8" fill="none" stroke="#76a845" stroke-width="2.5"/><rect x="25" y="23" width="8" height="8" fill="none" stroke="#76a845" stroke-width="2.5"/><path d="M11 9h18v14M11 27h14" stroke="#76a845" stroke-width="2.5" fill="none"/></svg>
    <h4>Professionalism</h4><p>Lorem ipsum dolor sit amet, consectetur adipiscing elit,</p>
  </div>
  <div class="point" style="left:370px;top:2880px">
    <svg class="ic" viewBox="0 0 36 36"><circle cx="18" cy="7" r="4" fill="#76a845"/><path d="M6 14h24M18 14v8l-7 10M18 22l7 10" stroke="#76a845" stroke-width="3" fill="none"/></svg>
    <h4>Expertise</h4><p>Lorem ipsum dolor sit amet, consectetur adipiscing elit,</p>
  </div>
  <div class="point" style="left:104px;top:2976px">
    <svg class="ic" viewBox="0 0 36 36"><circle cx="8" cy="12" r="4" fill="#76a845"/><path d="M2 26a6 6 0 0112 0z" fill="#76a845"/><path d="M18 12h16M18 19h16M18 26h12" stroke="#76a845" stroke-width="2.5"/></svg>
    <h4>Client Centric</h4><p>Lorem ipsum dolor sit amet, consectetur adipiscing elit,</p>
  </div>
  <div class="point" style="left:370px;top:2976px">
    <svg class="ic" viewBox="0 0 36 36"><circle cx="9" cy="8" r="4" fill="#76a845"/><circle cx="26" cy="6" r="4" fill="#76a845"/><path d="M9 13v20M26 11v22M4 18h10M21 16h10" stroke="#76a845" stroke-width="3"/></svg>
    <h4>Variety of Solutions</h4><p>Lorem ipsum dolor sit amet, consectetur adipiscing elit,</p>
  </div>

  <svg class="abs" style="left:640px;top:2615px" width="472" height="472" viewBox="0 0 472 472">
    <path d="M236 4 A232 232 0 0 1 468 236 A232 232 0 0 1 360 432" fill="none" stroke="#1f4b86" stroke-width="8"/>
    <path d="M20 200 A220 220 0 0 1 236 4" fill="none" stroke="#1f4b86" stroke-width="8"/>
  </svg>
  <div class="photo" role="img" aria-label="Smiling nurse in green scrubs" style="left:650px;top:2640px;width:440px;height:440px;border-radius:50%;background:radial-gradient(circle at 50% 40%,#e8e1d9,#9db3b0 70%,#6f8f89)"></div>
</section>

<section>
  <div class="abs testi-bg"></div>
  <div class="abs" style="left:0;top:3220px;width:1200px;display:flex;justify-content:center;align-items:center;gap:16px;font-size:11px;font-weight:600;color:var(--green)"><span style="width:50px;height:2px;background:var(--green)"></span>TESTIMONIALS<span style="width:50px;height:2px;background:var(--green)"></span></div>
  <h2 class="abs serif" style="left:0;top:3255px;width:1200px;text-align:center;font-size:38px">What Clients are Saying</h2>

  <div class="testi" style="left:90px">
    <div class="card"><div class="stars">★★★★★</div><p>Lorem ipsum dolor sit amet, consectetur adipiscing elit, sed do eiusmod tempor incididunt ut labore et dolore</p></div>
    <div class="avatar" role="img" aria-label="Client portrait"></div>
    <div class="quote">“</div>
    <div class="name">Dana Whitfield</div><div class="city">Los Angeles</div>
  </div>
  <div class="testi" style="left:440px">
    <div class="card"><div class="stars">★★★★★</div><p>Lorem ipsum dolor sit amet, consectetur adipiscing elit, sed do eiusmod tempor incididunt ut labore et dolore</p></div>
    <div class="avatar" role="img" aria-label="Client portrait"></div>
    <div class="quote">“</div>
    <div class="name">Dana Whitfield</div><div class="city">Los Angeles</div>
  </div>
  <div class="testi" style="left:788px">
    <div class="card"><div class="stars">★★★★★</div><p>Lorem ipsum dolor sit amet, consectetur adipiscing elit, sed do eiusmod tempor incididunt ut labore et dolore</p></div>
    <div class="avatar" role="img" aria-label="Client portrait"></div>
    <div class="quote">“</div>
    <div class="name">Dana Whitfield</div><div class="city">Los Angeles</div>
  </div>
</section>

<section>
  <div class="photo connect-photo" role="img" aria-label="Bright clinic interior background"></div>
  <div class="photo connect-figure" role="img" aria-label="Woman in a white blouse reading a tablet"></div>
  <div class="abs connect-card">
    <h2>Connect With Us</h2>
    <p>Lorem ipsum dolor sit amet, consectetur adipiscing elit,<br>sed do eiusmod tempor incididunt ut</p>
    <div class="field">NAME</div>
    <div class="field">EMAIL</div>
    <div class="field">MESSAGE</div>
    <div class="book">BOOK ONLINE</div>
  </div>
</section>

<footer>
  <div class="abs footer-bg"></div>
  <div class="abs footer-logo">VELMO</div>
  <div class="abs" style="left:112px;top:4674px;font-size:14px;color:var(--navy)">Follow Us</div>
  <span class="social" style="left:194px"></span>
  <span class="social" style="left:230px"></span>
  <span class="social" style="left:266px"></span>

  <div class="f-title" style="left:364px;width:120px">Quick Links</div>
  <div class="f-list" style="left:364px;top:4594px">Home<br>About us<br>Limitation of Liability<br>Privacy Policy</div>

  <div class="f-title" style="left:585px;width:120px">Contact</div>
  <div class="f-row" style="left:602px;top:4598px"><svg width="14" height="18" viewBox="0 0 14 18"><path d="M7 0a7 7 0 00-7 7c0 5 7 11 7 11s7-6 7-11a7 7 0 00-7-7z" fill="#76a845"/><circle cx="7" cy="7" r="2.5" fill="#fff"/></svg><span>1234 Location<br>1456 Street</span></div>
  <div class="f-row" style="left:602px;top:4656px"><svg width="16" height="16" viewBox="0 0 24 24"><path d="M6.6 10.8a15 15 0 006.6 6.6l2.2-2.2a1 1 0 011-.25 11.4 11.4 0 003.6.6 1 1 0 011 1V20a1 1 0 01-1 1A17 17 0 013 4a1 1 0 011-1h3.5a1 1 0 011 1 11.4 11.4 0 00.6 3.6 1 1 0 01-.25 1z" fill="#76a845"/></svg><span>1-800-555-0199</span></div>
  <div class="f-row" style="left:602px;top:4694px"><svg width="16" height="12" viewBox="0 0 16 12"><rect width="16" height="12" fill="#76a845"/><path d="M1 1l7 5 7-5" fill="none" stroke="#fff" stroke-width="1.5"/></svg><span>hello@velmo.example</span></div>

  <div class="f-title" style="left:859px;width:246px">Join our Newsletter</div>
  <div class="f-list" style="left:859px;top:4598px;line-height:20px;width:230px">Sign up for our newsletter to know the latest from us</div>
  <div class="abs newsletter"><span>Email</span><b>SUBSCRIBE</b></div>

  <div class="abs footer-rule"></div>
  <div class="abs copyright">VELMO HYDRATION</div>
</footer>

</body>
</html>
```